Graphic Design for an online custom wine label company

Provides artistic and funky wine labels to people online. People can customize the text on the label.

```html
<!DOCTYPE html>
<html lang="en">
<head>
<meta charset="utf-8">
<title>Wine Label</title>
<link rel="stylesheet" href="https://fonts.googleapis.com/css2?family=Yellowtail&family=Arimo:ital,wght@0,400;0,700;1,400&family=Roboto:wght@300;700&display=swap">
<style>
  :root {
    --label-night: #000000;
    --label-sky: #00aeef;
    --title-blue: #1ba6e6;
    --text-white: #ffffff;
    --mascot-blue: #9bbad0;
    --mascot-shadow: #4d6674;
  }
  * { margin: 0; padding: 0; box-sizing: border-box; }
  html, body {
    width: 840px;
    height: 1200px;
    overflow: hidden;
    background: var(--label-night);
  }
  .label {
    position: relative;
    width: 840px;
    height: 1200px;
    background: var(--label-night);
    overflow: hidden;
  }
  .mascot {
    position: absolute;
    left: 243px;
    top: 68px;
    width: 356px;
    height: 556px;
  }
  .wine-name {
    position: absolute;
    left: 0;
    top: 672px;
    width: 840px;
    text-align: center;
    font-family: "Yellowtail", cursive;
    font-size: 104px;
    line-height: 1;
    color: var(--title-blue);
  }
  .wine-story {
    position: absolute;
    left: 0;
    top: 810px;
    width: 840px;
    text-align: center;
    font-family: "Arimo", sans-serif;
    font-style: italic;
    font-size: 25.5px;
    line-height: 41px;
    color: var(--text-white);
  }
  .wine-story span { display: block; }
  .details-band {
    position: absolute;
    left: 0;
    top: 958px;
    width: 840px;
    height: 242px;
    background: var(--label-sky);
    color: var(--text-white);
  }
  .vintage {
    position: absolute;
    left: 0;
    top: 35px;
    width: 840px;
    text-align: center;
    font-family: "Roboto", sans-serif;
    font-weight: 300;
    font-size: 43px;
    letter-spacing: 2px;
    line-height: 1;
  }
  .wine-type {
    position: absolute;
    left: 0;
    top: 93px;
    width: 840px;
    text-align: center;
    font-family: "Arimo", sans-serif;
    font-weight: 700;
    font-size: 33px;
    letter-spacing: 1px;
    line-height: 1;
  }
  .volume, .origin {
    position: absolute;
    top: 178px;
    font-family: "Arimo", sans-serif;
    font-size: 29px;
    line-height: 1;
  }
  .volume { left: 72px; }
  .origin { right: 73px; }
</style>
</head>
<body>
  <main class="label">
    <svg class="mascot" viewBox="0 0 356 556" role="img" aria-label="Illustration: cheerful cartoon cow standing and raising a glass of red wine with small hearts above it">
      <defs>
        <radialGradient id="mascotTone" cx="50%" cy="45%" r="60%">
          <stop offset="0%" stop-color="var(--mascot-blue)"/>
          <stop offset="100%" stop-color="var(--mascot-shadow)"/>
        </radialGradient>
      </defs>
      <rect x="0" y="0" width="356" height="556" rx="28" fill="url(#mascotTone)"/>
    </svg>

    <h1 class="wine-name">Name of Wine</h1>

    <p class="wine-story">
      <span>Idunt luptat, venim nim volortie veriust ionsecte tate</span>
      <span>magna feugait, quiscipit vel eugue tat, velendignim</span>
      <span>nero tilicit illarissulus conte nime receps, Eperfenem</span>
    </p>

    <section class="details-band">
      <p class="vintage">SELECTION 2012</p>
      <p class="wine-type">TYPE OF WINE</p>
      <p class="volume">XXX ml</p>
      <p class="origin">PRODUCT OF CITY</p>
    </section>
  </main>
</body>
</html>
```